Vodka Soda brand identity design and label design

New vodka soda (hard seltzer) brand needs a brand identity design and label designs.

The brand name is VELMO

We produce vodka soda packaged in cans. They come in three flavours
- Raspberry and Lime
- Pina Colada
- Black Cherry

We would like to have the designs look similar (same template) but have one difference depending on the fruit flavour.

The final delivered package should contain
- brand identity design guide with a logo, font and colour schemes
- 3 label designs on the same template (label size 8.125 x 5 inches)

Some example designs of similar products are attached to the project.

Target Market(s)

Gender neutral, younger population

Colors
000000

Requirements
Must have
• Bright background and bright eye catching colours.

```html
<!DOCTYPE html>
<html lang="en">
<head>
<meta charset="utf-8">
<title>VELMO Hard Seltzer – Label Range</title>
<link href="https://fonts.googleapis.com/css2?family=Rubik:wght@500;700;800&family=Montserrat:wght@500;700&display=swap" rel="stylesheet">
<style>
  :root {
    --ink: #1c1c1c;
    --paper: #f7f7f7;
    --stage: #e4e4e4;
    --white: #ffffff;
    --pina: #e9b80c;
    --pina-deep: #c99a06;
    --cherry: #6c1420;
    --cherry-deep: #3e0a10;
    --berry: #cf2430;
    --berry-deep: #a9151f;
    --lime: #1ec41e;
    --art-tone: #dcdcdc;
  }
  * { box-sizing: border-box; margin: 0; padding: 0; }
  html, body { width: 1200px; height: 1070px; overflow: hidden; }
  body { background: var(--stage); font-family: "Rubik", sans-serif; }

  .label-range {
    position: relative;
    width: 1200px; height: 1070px;
    display: flex; gap: 30px;
    padding: 55px 30px;
  }
  .label {
    position: relative;
    width: 360px; height: 960px;
    background: var(--paper);
    overflow: hidden;
    box-shadow: 0 6px 20px rgba(0,0,0,0.12);
  }
  .label--pina   { --accent: var(--pina);   --accent-deep: var(--pina-deep);   --headline: var(--pina); }
  .label--cherry { --accent: var(--cherry); --accent-deep: var(--cherry-deep); --headline: var(--cherry); }
  .label--berry  { --accent: var(--berry);  --accent-deep: var(--berry-deep);  --headline: var(--lime); }

  .tagline-band {
    position: absolute; left: 0; top: 0;
    width: 100%; height: 62px;
    background: var(--accent);
    color: var(--white);
    font-family: "Montserrat", sans-serif;
    font-weight: 700; font-size: 15px;
    white-space: nowrap;
    display: flex; align-items: center;
    padding-left: 14px;
    letter-spacing: 0.3px;
  }
  .tagline-rule {
    position: absolute; left: 0; top: 72px;
    width: 100%; height: 5px;
    background: var(--accent);
  }
  .label--berry .tagline-rule { background: var(--lime); }

  .brand-name {
    position: absolute; left: -8px; top: 110px;
    height: 600px;
    writing-mode: vertical-rl;
    transform: rotate(180deg);
    font-weight: 800;
    font-size: 150px;
    line-height: 1;
    color: var(--ink);
    text-align: center;
    letter-spacing: -2px;
  }

  .flavour-art {
    position: absolute; left: 175px; top: 150px;
    width: 160px; height: 400px;
    border-radius: 80px;
    background: radial-gradient(circle at 50% 45%, var(--art-tone), rgba(220,220,220,0.25) 70%);
  }

  .product-type {
    position: absolute; left: 160px; top: 610px;
    font-weight: 700; font-size: 42px;
    line-height: 1;
    color: var(--headline);
    white-space: nowrap;
  }

  .flavour-panel {
    position: absolute; left: 0; top: 710px;
    width: 100%; height: 250px;
    background: linear-gradient(180deg, var(--accent), var(--accent-deep));
    color: var(--white);
    text-align: center;
  }
  .flavour-name {
    margin-top: 34px;
    font-weight: 800; font-size: 31px;
    letter-spacing: 0.5px;
    white-space: nowrap;
    height: 38px; line-height: 38px;
  }
  .label--berry .flavour-name { font-size: 27px; }

  .stats {
    margin-top: 22px;
    display: flex; justify-content: center; align-items: stretch;
  }
  .stat { padding: 0 12px; display: flex; flex-direction: column; align-items: center; }
  .stat + .stat { border-left: 2px solid var(--white); }
  .stat-value { font-weight: 800; font-size: 38px; line-height: 1; }
  .stat-unit { font-family: "Montserrat", sans-serif; font-weight: 500; font-size: 11px; letter-spacing: 1px; margin-top: 2px; }

  .volume {
    margin-top: 34px;
    font-family: "Montserrat", sans-serif;
    font-weight: 500; font-size: 24px;
    letter-spacing: 1px;
  }
</style>
</head>
<body>
<main class="label-range">

  <section class="label label--pina">
    <div class="tagline-band">LOREM IPSUM DOLOR SIT &nbsp;●&nbsp; LOREM IPSUM DOLOR SIT &nbsp;●</div>
    <div class="tagline-rule"></div>
    <h1 class="brand-name">VELMO</h1>
    <div class="flavour-art" role="img" aria-label="Grey line illustration of a pina colada glass with straw and citrus slice"></div>
    <p class="product-type">HARD<br>SELTZER</p>
    <div class="flavour-panel">
      <h2 class="flavour-name">PINA COLADA</h2>
      <div class="stats">
        <div class="stat"><span class="stat-value">7%</span><span class="stat-unit">ALCOHOL</span></div>
        <div class="stat"><span class="stat-value">100</span><span class="stat-unit">CALORIES</span></div>
      </div>
      <p class="volume">500ml</p>
    </div>
  </section>

  <section class="label label--cherry">
    <div class="tagline-band">LOREM IPSUM DOLOR SIT &nbsp;●&nbsp; LOREM IPSUM DOLOR SIT &nbsp;●</div>
    <div class="tagline-rule"></div>
    <h1 class="brand-name">VELMO</h1>
    <div class="flavour-art" role="img" aria-label="Grey line illustration of two cherries on a stem"></div>
    <p class="product-type">HARD<br>SELTZER</p>
    <div class="flavour-panel">
      <h2 class="flavour-name">BLACK CHERRY</h2>
      <div class="stats">
        <div class="stat"><span class="stat-value">7%</span><span class="stat-unit">ALCOHOL</span></div>
        <div class="stat"><span class="stat-value">100</span><span class="stat-unit">CALORIES</span></div>
      </div>
      <p class="volume">500ml</p>
    </div>
  </section>

  <section class="label label--berry">
    <div class="tagline-band">LOREM IPSUM DOLOR SIT &nbsp;●&nbsp; LOREM IPSUM DOLOR SIT &nbsp;●</div>
    <div class="tagline-rule"></div>
    <h1 class="brand-name">VELMO</h1>
    <div class="flavour-art" role="img" aria-label="Grey line illustration of a raspberry and a lime slice"></div>
    <p class="product-type">HARD<br>SELTZER</p>
    <div class="flavour-panel">
      <h2 class="flavour-name">RASPBERRY &amp; LIME</h2>
      <div class="stats">
        <div class="stat"><span class="stat-value">7%</span><span class="stat-unit">ALCOHOL</span></div>
        <div class="stat"><span class="stat-value">100</span><span class="stat-unit">CALORIES</span></div>
      </div>
      <p class="volume">500ml</p>
    </div>
  </section>

</main>
</body>
</html>
```